Business card design for global fintech startup

Verdell is a modern payments platform for the global insurance industry, serving international health, life, and travel insurers, MGAs, brokers, and partners.

We need a professional, premium business card for use at insurance conferences and executive meetings. The goal is to create a card that feels trustworthy, modern, and high-quality, while still being distinctive and memorable in a stack of business cards.

Target audience:
Senior insurance executives (VP, C-suite).

Design goals:
Clear, professional, and credible
Modern but not trendy
Premium and well-structured
Easy to read and practical for networking

Brand direction:
Brand-first (company over individual)
Follow existing brand guidelines where possible
Clean layout, strong hierarchy, excellent readability

Must include:
Name
Title
Company name (Verdell)
Logo
Email
Phone/Whatsapp
Website (www.joinverdell.com)
Tagline - Payments built on trust

Materials & finish:
Open to designer recommendations for premium look and feel.

Please avoid:
Flashy or trendy startup styles
Generic insurance icons or clichés
Cluttered layouts or hard-to-read text

Deliverables:
Front and back business card, print-ready files.

Target Market(s)

Global Insurance executives

Industry/Entity Type

Fintech, Insurtech, Insurance, Financial Services

Contact Information for Business Card

Name Title Company name (Verdell) Logo Email Phone/Whatsapp Website (www.joinverdell.com) Tagline - Payments built on trust

Font styles to use
Other font styles liked:
• See brand guidelines

Requirements
Nice to have
• something that stands out/makes us more memorable while still remaining professional
Should not have
• Please avoid: Flashy or trendy startup styles Generic insurance icons or clichés Cluttered layouts or hard-to-read text

```html
<!DOCTYPE html>
<html lang="en">
<head>
<meta charset="utf-8">
<title>Verdell business card, front and back</title>
<link href="https://fonts.googleapis.com/css2?family=Ubuntu:wght@400;500;700&display=swap" rel="stylesheet">
<style>
  :root {
    --canvas: #e6e6e8;
    --paper: #f4f4f3;
    --ink: #1b1a1c;
    --ink-soft: #5b5b60;
    --rule: #4a4a4e;
    --violet: #5a4ba3;
    --icon: #4b4a9a;
    --orange: #e2731f;
    --amber: #ecb444;
    --purple: #5e4a9f;
    --blue: #2e7fc0;
    --cyan: #2bb3d9;
    --tag-text: #fdf4e6;
  }
  * { margin: 0; padding: 0; box-sizing: border-box; }
  html, body {
    width: 1200px; height: 955px; overflow: hidden;
    background: var(--canvas);
    font-family: "Ubuntu", sans-serif;
  }
  .canvas { position: relative; width: 1200px; height: 955px; }
  .card {
    position: absolute; left: 333px; width: 551px; height: 314px;
    background: var(--paper);
    box-shadow: 0 6px 14px rgba(0,0,0,0.18);
    overflow: hidden;
  }
  .card--front { top: 141px; }
  .card--back { top: 513px; }

  .brand { position: absolute; display: flex; align-items: center; color: var(--ink); font-weight: 500; }
  .brand__mark { border-radius: 50%; background: var(--violet); flex: none; }
  .brand--front { left: 34px; top: 34px; gap: 16px; font-size: 38px; letter-spacing: 2.5px; }
  .brand--front .brand__mark { width: 36px; height: 36px; }
  .brand--back { left: 0; right: 0; top: 0; bottom: 0; justify-content: center; gap: 20px; font-size: 50px; letter-spacing: 3px; }
  .brand--back .brand__mark { width: 48px; height: 48px; }

  .person { position: absolute; left: 33px; top: 144px; right: 34px; }
  .person__name { font-size: 20px; font-weight: 500; color: var(--violet); line-height: 1; }
  .person__role { display: flex; align-items: center; gap: 7px; margin-top: 7px; }
  .person__title { font-size: 12.5px; color: var(--ink-soft); white-space: nowrap; }
  .person__rule { flex: 1; height: 1px; background: var(--rule); margin-top: 5px; }

  .contacts { position: absolute; left: 34px; top: 209px; list-style: none; }
  .contacts li { display: flex; align-items: center; gap: 11px; height: 17.5px; font-size: 12.5px; color: #3a3a40; }
  .contacts svg { width: 11px; height: 11px; flex: none; }

  .tagline {
    position: absolute; left: 320px; top: 237px; width: 231px; height: 33px;
    background: linear-gradient(90deg, var(--orange), var(--amber));
    display: flex; align-items: center; justify-content: center;
    color: var(--tag-text); font-size: 11.5px; font-weight: 700; letter-spacing: 0.6px;
    white-space: nowrap;
  }
  .stripe-thin {
    position: absolute; left: 0; right: 0; top: 290px; height: 4px;
    background: linear-gradient(90deg, var(--orange), var(--amber));
  }
  .stripe-band {
    position: absolute; left: 0; right: 0; top: 297px; height: 17px;
    background: linear-gradient(90deg, var(--purple), var(--blue) 55%, var(--cyan));
  }
</style>
</head>
<body>
<main class="canvas">
  <section class="card card--front" aria-label="Card front">
    <div class="brand brand--front"><span class="brand__mark"></span><span class="brand__name">VERDELL</span></div>

    <div class="person">
      <p class="person__name">Daniel Reyes</p>
      <div class="person__role">
        <span class="person__title">Chief Executive Officer</span>
        <span class="person__rule"></span>
      </div>
    </div>

    <ul class="contacts">
      <li>
        <svg viewBox="0 0 12 12" aria-hidden="true"><circle cx="6" cy="6" r="6" fill="var(--icon)"/><path d="M4 3.2l1 1.3-.5.8c.4.8 1 1.4 1.8 1.8l.8-.5 1.3 1-.6 1.1C5.7 8.6 3.4 6.3 3.3 4z" fill="#fff"/></svg>
        <span>+44 20 7946 0318</span>
      </li>
      <li>
        <svg viewBox="0 0 12 12" aria-hidden="true"><rect x="0.5" y="2" width="11" height="8" fill="var(--icon)"/><path d="M1 2.6l5 4 5-4M1 9.5l3.6-3.3M11 9.5L7.4 6.2" stroke="#fff" stroke-width="0.9" fill="none"/></svg>
        <span>dreyes@joinverdell.com</span>
      </li>
      <li>
        <svg viewBox="0 0 12 12" aria-hidden="true"><circle cx="6" cy="6" r="5.3" fill="none" stroke="var(--icon)" stroke-width="1"/><ellipse cx="6" cy="6" rx="2.3" ry="5.3" fill="none" stroke="var(--icon)" stroke-width="0.9"/><path d="M0.8 6h10.4M1.8 3.4h8.4M1.8 8.6h8.4" stroke="var(--icon)" stroke-width="0.8"/></svg>
        <span>www.joinverdell.com</span>
      </li>
    </ul>

    <div class="tagline">Payments built on trust</div>
    <div class="stripe-thin"></div>
    <div class="stripe-band"></div>
  </section>

  <section class="card card--back" aria-label="Card back">
    <div class="brand brand--back"><span class="brand__mark"></span><span class="brand__name">VERDELL</span></div>
  </section>
</main>
</body>
</html>
```